Build a Web page - Dovin Pratchell Homes, LLC - a custom home builder

We are a custom home builder in Wisconsin. Need a basic web page with a home page, About Us, Contact info, Gallery, and Testimonials page. Gallery will probably have sub-pages and each will have about ten pictures or less. I already own the domain and have web hosting through Wix, I just need the site built. Once the page is built I should be able to do the upkeep on it myself. If I need to add pictures or whatever.
Updates

Project Deadline Extended
Reason: I am still looking through designs and will select soon - thank you!

Target Market(s)

Gen X and Millennials who are looking to build a home. Custom built homes - not generic spec homes.

Industry/Entity Type

Home Builder

Number of Pages Required

5+ page

Font styles to use
Sans Serif

Colors
ffffff
ec1f27
000000
9d9d9d

Requirements
Must have
• I have no idea if I want coded or in coded. I'm not sure of the difference and why I would want one over the other.
Nice to have
• We like the following colors - red, black, gray, white.
Should not have
• not a big fan of clip art like hammers, tape measures, etc. Must look professional.

```html
<!DOCTYPE html>
<html lang="en">
<head>
<meta charset="utf-8">
<title>Dovin Pratchell Homes — Custom Home Builder</title>
<link href="https://fonts.googleapis.com/css2?family=Lato:wght@400;700&family=Oswald:wght@300;400&display=swap" rel="stylesheet">
<style>
:root{
  --red:#9e0f12;
  --red-bright:#b5161b;
  --ink:#1f1f1f;
  --text:#444;
  --grey:#9d9d9d;
  --grey-dark:#6f6f6f;
  --grey-bg:#ececec;
  --white:#ffffff;
  --footer:#2a2a2a;
  --footer-line:#3b3b3b;
}
*{box-sizing:border-box;margin:0;padding:0}
html,body{width:1200px;height:3093px;overflow:hidden}
body{font-family:"Lato",sans-serif;color:var(--text);background:var(--white);position:relative}

/* header */
.site-header{position:absolute;left:0;top:0;width:1200px;height:146px;background:var(--white)}
.topbar{position:absolute;left:495px;top:0;width:705px;height:41px;background:#6d6d6d;clip-path:polygon(40px 0,100% 0,100% 100%,0 100%);display:flex;align-items:center;padding-left:80px;gap:26px;color:var(--white);font-size:17px;white-space:nowrap}
.topbar .item{display:flex;align-items:center;gap:10px}
.topbar .ico{width:26px;height:26px;background:var(--red);display:flex;align-items:center;justify-content:center}
.social{display:flex;gap:8px}
.social span{width:28px;height:28px;background:var(--red);display:block}
.topbar .social{margin-left:28px}
.brand{position:absolute;left:78px;top:40px;display:flex;align-items:center;gap:12px}
.brand .mark{width:26px;height:26px;background:var(--red)}
.brand .name{font-family:"Lato",sans-serif;font-weight:700;font-size:24px;color:var(--red);line-height:1.05;width:140px}
.main-nav{position:absolute;right:80px;top:94px;display:flex;font-size:16px;color:var(--ink);text-transform:uppercase;white-space:nowrap}
.main-nav a{color:inherit;text-decoration:none;padding:0 31px;border-left:1px solid #ccc;line-height:20px}
.main-nav a:first-child{border-left:none;color:var(--red);text-decoration:underline;text-underline-offset:6px}
.main-nav a:last-child{padding-right:0}

/* hero */
.hero{position:absolute;left:0;top:146px;width:1200px;height:516px;background:linear-gradient(180deg,#c9cdd1 0%,#a79b8c 40%,#7a6e5e 62%,#5f7a3f 80%,#4d6b30 100%)}
.hero .arrow{position:absolute;top:208px;width:40px;height:36px;background:#3a3a3a;display:flex;align-items:center;justify-content:center}
.hero .caption{position:absolute;left:0;bottom:0;width:100%;height:54px;background:rgba(40,40,40,.72);color:var(--white);font-family:"Oswald",sans-serif;font-weight:300;font-size:30px;letter-spacing:3px;text-align:center;line-height:54px;white-space:nowrap}

/* shared heading */
.section-title{font-family:"Oswald",sans-serif;font-weight:400;font-size:40px;text-align:center;text-transform:uppercase;color:var(--grey-dark);line-height:1}
.section-title b{color:var(--red);font-weight:400}
.divider{display:block;margin:14px auto 0;width:28px;height:10px;background:repeating-linear-gradient(110deg,var(--grey) 0 4px,transparent 4px 8px)}
.btn{display:inline-block;border:3px double #777;background:#666;color:var(--white);font-size:15px;font-weight:700;padding:10px 22px;white-space:nowrap}

/* welcome */
.welcome{position:absolute;left:0;top:662px;width:1200px;height:365px;text-align:center}
.welcome .section-title{margin-top:42px}
.welcome p{width:1030px;margin:26px auto 0;font-size:15px;line-height:29px;color:var(--text)}
.welcome .btn{margin-top:24px}

/* gallery */
.gallery{position:absolute;left:0;top:1027px;width:1200px;height:761px;background:var(--grey-bg);text-align:center}
.gallery .section-title{margin-top:47px}
.tabs{position:absolute;left:110px;top:146px;display:flex;gap:24px}
.tabs span{width:178px;height:44px;background:#777;color:var(--white);font-size:18px;font-weight:700;line-height:44px;clip-path:polygon(10px 0,100% 0,calc(100% - 10px) 100%,0 100%);position:relative}
.tabs span.active{background:var(--red)}
.grid{position:absolute;left:80px;top:223px;width:1040px;display:grid;grid-template-columns:repeat(4,254px);grid-auto-rows:202px;gap:6px 8px}
.tile{position:relative}
.tile .overlay{position:absolute;inset:0;background:rgba(30,30,30,.7);color:var(--white);display:flex;flex-direction:column;align-items:center;padding-top:20px}
.tile .overlay h3{font-family:"Oswald",sans-serif;font-weight:400;font-size:28px;margin-top:12px}
.tile .overlay p{font-size:13px;line-height:17px;width:170px;margin-top:6px}
.gallery .btn{position:absolute;left:540px;top:668px}

/* testimonials */
.testimonials{position:absolute;left:0;top:1788px;width:1200px;height:505px;background:linear-gradient(180deg,#2f3540 0%,#3b4250 50%,#262b33 100%)}
.testimonials .section-title{color:var(--white);margin-top:40px}
.card{position:absolute;top:192px;width:328px;height:222px;background:var(--white);text-align:center}
.card .quote{position:absolute;left:115px;top:-48px;width:97px;height:99px;background:var(--red);display:flex;align-items:center;justify-content:center}
.card h4{margin-top:72px;color:var(--red);font-size:17px;font-weight:400}
.card .stars{color:var(--red);font-size:14px;letter-spacing:3px;margin-top:4px}
.card p{font-size:14px;line-height:24px;width:290px;margin:8px auto 0}
.card .plus{position:absolute;left:142px;bottom:-22px;width:44px;height:44px;border-radius:50%;background:var(--red);color:var(--white);font-size:20px;line-height:24px;clip-path:inset(0 0 50% 0)}
.dots{position:absolute;left:574px;top:451px;display:flex;gap:6px}
.dots i{width:9px;height:9px;border:1px solid var(--white);border-radius:50%}
.dots i.on{background:var(--red);border-color:var(--red)}

/* why */
.why{position:absolute;left:0;top:2293px;width:1200px;height:425px;text-align:center}
.why .section-title{margin-top:43px}
.feature{position:absolute;top:142px;width:250px;text-align:center}
.feature .icon{width:118px;height:118px;border:2px solid #555;margin:0 auto;display:flex;align-items:center;justify-content:center}
.feature h4{font-size:22px;color:var(--ink);margin-top:36px;letter-spacing:1px;font-weight:400;white-space:nowrap}
.feature p{font-size:14px;line-height:21px;margin:8px auto 0;width:210px;color:#333}

/* footer */
.site-footer{position:absolute;left:0;top:2718px;width:1200px;height:319px;background:var(--footer);color:#ddd}
.site-footer h5{font-weight:400;font-size:21px;color:var(--white);text-transform:uppercase;padding-bottom:14px;border-bottom:1px solid var(--footer-line);white-space:nowrap}
.col{position:absolute;top:46px}
.links li{list-style:none;font-size:14px;line-height:36px}
.links li::before{content:"•";margin-right:10px}
.contact .row{display:flex;gap:12px;font-size:14px;line-height:20px;margin-top:14px}
.contact .row svg{flex:none}
.map{position:absolute;left:625px;top:105px;width:495px;height:167px;border:5px solid var(--white);background:linear-gradient(135deg,#c9d8e8 0%,#e6e2d4 45%,#b9cfe0 70%,#dfe6cf 100%)}
.bottombar{position:absolute;left:0;top:3037px;width:1200px;height:56px;background:var(--red);color:var(--white);font-size:14px;display:flex;align-items:center;justify-content:space-between;padding:0 80px}
.bottombar .social span{background:transparent;border:1px solid rgba(255,255,255,.7)}
</style>
</head>
<body>

<header class="site-header">
  <div class="topbar">
    <div class="item"><span class="ico"><svg width="14" height="14" viewBox="0 0 24 24"><path fill="#fff" d="M6.6 10.8a15 15 0 0 0 6.6 6.6l2.2-2.2c.3-.3.7-.4 1-.2 1.1.4 2.3.6 3.6.6.6 0 1 .4 1 1V20c0 .6-.4 1-1 1A17 17 0 0 1 3 4c0-.6.4-1 1-1h3.5c.6 0 1 .4 1 1 0 1.3.2 2.5.6 3.6.1.3 0 .7-.2 1z"/></svg></span>123 456 7890</div>
    <div class="item"><span class="ico"><svg width="14" height="12" viewBox="0 0 24 18"><path fill="#fff" d="M0 0h24v18H0z"/><path fill="none" stroke="#9e0f12" stroke-width="2" d="M1 1l11 9 11-9"/></svg></span>info@dovinpratchellhomes.com</div>
    <div class="social"><span></span><span></span><span></span></div>
  </div>
  <div class="brand"><span class="mark"></span><span class="name">Dovin Pratchell Homes</span></div>
  <nav class="main-nav"><a>Home</a><a>About Us</a><a>Gallery</a><a>Testimonials</a><a>Contact Us</a></nav>
</header>

<section class="hero" role="img" aria-label="Photo of a custom-built single-storey home with stone front, lawn and young tree">
  <span class="arrow" style="left:4px"><svg width="12" height="14" viewBox="0 0 12 14"><path d="M9 1 3 7l6 6" stroke="#fff" stroke-width="3" fill="none"/></svg></span>
  <span class="arrow" style="right:4px"><svg width="12" height="14" viewBox="0 0 12 14"><path d="m3 1 6 6-6 6" stroke="#fff" stroke-width="3" fill="none"/></svg></span>
  <div class="caption">WE ARE A CUSTOM HOME BUILDER IN WISCONSIN, USA</div>
</section>

<section class="welcome">
  <h1 class="section-title"><b>Welcome to Dovin</b> Pratchell Homes</h1>
  <span class="divider"></span>
  <p>Sed ut perspiciatis unde omnis iste natus error site voluptatem accusantium doloremque laudantium, totam rem aperiam, eaque ipsa quae ab illo inventore veritatis et quasirrwtu architecto beatae vitae dicta sunt explicabo. Nemo enim ipsam voluptatem quia voluptas sit aspernatur aut odit aut fugit, sed quia consequuntur magninie dolores eos qui ratione voluptatem sequi nesciunt. Neque porro quisquam est, quie dolorem ipsum quia dolor sit amet, consectetur, adipisci velit, sed quia non numquam eius modi tempora incidunt uter labore et dolore .</p>
  <span class="btn">Read More &nbsp;»</span>
</section>

<section class="gallery">
  <h2 class="section-title"><b>Project</b> Gallery</h2>
  <span class="divider"></span>
  <div class="tabs"><span class="active">View All</span><span>Annie</span><span>Cassey</span><span>Dr</span><span>Tara</span></div>
  <div class="grid">
    <div class="tile" role="img" aria-label="Kitchen interior with wood cabinets" style="background:linear-gradient(135deg,#6b4a2e,#a07b54)">
      <div class="overlay">
        <svg width="40" height="40" viewBox="0 0 40 40" fill="none" stroke="#fff" stroke-width="2.5"><path d="M4 14V4h10M26 4h10v10M36 26v10H26M14 36H4V26M4 4l12 12M36 4 24 16M36 36 24 24M4 36l12-12"/></svg>
        <h3>ANNIE</h3>
        <p>Duis autem vel eum iriure dolor in hendrerit morein vulputate.</p>
      </div>
    </div>
    <div class="tile" role="img" aria-label="Hallway leading to a kitchen" style="background:linear-gradient(135deg,#d8cdb8,#8a5e3a)"></div>
    <div class="tile" role="img" aria-label="Living room with fireplace and ceiling fan" style="background:linear-gradient(135deg,#c9d2d4,#6d6152)"></div>
    <div class="tile" role="img" aria-label="Family room with sofas and television" style="background:linear-gradient(135deg,#d9c8a2,#7a2f24)"></div>
    <div class="tile" role="img" aria-label="Tiled fireplace with wood mantel" style="background:linear-gradient(135deg,#8a6540,#c9a77c)"></div>
    <div class="tile" role="img" aria-label="Backyard wooden deck" style="background:linear-gradient(180deg,#d8dcd8,#7a3e2e 70%,#6b8a4a)"></div>
    <div class="tile" role="img" aria-label="Kitchen with island and dining table" style="background:linear-gradient(135deg,#7a4a28,#c99a66)"></div>
    <div class="tile" role="img" aria-label="Bright bathroom with white vanity" style="background:linear-gradient(135deg,#e8e8e4,#a9aba4)"></div>
  </div>
  <span class="btn">View All &nbsp;»</span>
</section>

<section class="testimonials" role="group" aria-label="Customer testimonials over a photo of a couple in front of their home">
  <h2 class="section-title">What Our Customer Say</h2>
  <span class="divider"></span>
  <div class="card" style="left:80px"><span class="quote"><svg width="34" height="28" viewBox="0 0 34 28"><path fill="#fff" d="M0 14C0 5 5 0 13 0v6c-4 0-6 3-6 7h6v15H0zM21 14c0-9 5-14 13-14v6c-4 0-6 3-6 7h6v15H21z"/></svg></span><h4>Renato Calles</h4><div class="stars">★★★★★</div><p>Duis autem vel eum iriure dolor in hendrerit in vulputate velit esse molestie conat vero eros et accumsan et iusto.</p><span class="plus">+</span></div>
  <div class="card" style="left:435px"><span class="quote"><svg width="34" height="28" viewBox="0 0 34 28"><path fill="#fff" d="M0 14C0 5 5 0 13 0v6c-4 0-6 3-6 7h6v15H0zM21 14c0-9 5-14 13-14v6c-4 0-6 3-6 7h6v15H21z"/></svg></span><h4>Derek Marlow</h4><div class="stars">★★★★★</div><p>Duis autem vel eum iriure dolor in hendrerit in vulputate velit esse molestie conat vero eros et accumsan et iusto.</p><span class="plus">+</span></div>
  <div class="card" style="left:790px"><span class="quote"><svg width="34" height="28" viewBox="0 0 34 28"><path fill="#fff" d="M0 14C0 5 5 0 13 0v6c-4 0-6 3-6 7h6v15H0zM21 14c0-9 5-14 13-14v6c-4 0-6 3-6 7h6v15H21z"/></svg></span><h4>Bryce Okonne</h4><div class="stars">★★★★★</div><p>Duis autem vel eum iriure dolor in hendrerit in vulputate velit esse molestie conat vero eros et accumsan et iusto.</p><span class="plus">+</span></div>
  <div class="dots"><i></i><i></i><i></i><i class="on"></i></div>
</section>

<section class="why">
  <h2 class="section-title"><b>Why</b> Choose Us</h2>
  <span class="divider"></span>
  <div class="feature" style="left:62px">
    <div class="icon"><svg width="60" height="66" viewBox="0 0 60 66"><circle cx="26" cy="26" r="24" fill="#9e0f12"/><text x="26" y="36" text-anchor="middle" font-family="Lato,sans-serif" font-weight="700" font-size="28" fill="#fff">$</text><path d="M44 30v20h-8l14 14 14-14h-8V30z" fill="#9e0f12" stroke="#fff" stroke-width="2" transform="translate(-6 0)"/></svg></div>
    <h4>Low Cost</h4><p>Duis autem vel eum iriure dolor in hendrerit in vulputate velit esse molestie conat .</p>
  </div>
  <div class="feature" style="left:336px">
    <div class="icon"><svg width="72" height="72" viewBox="0 0 72 72"><circle cx="36" cy="36" r="33" fill="none" stroke="#9e0f12" stroke-width="3"/><circle cx="36" cy="36" r="25" fill="none" stroke="#9e0f12" stroke-width="2"/><rect x="6" y="30" width="60" height="12" fill="#9e0f12"/></svg></div>
    <h4>100% Satisfaction</h4><p>Duis autem vel eum iriure dolor in hendrerit in vulputate velit esse molestie conat .</p>
  </div>
  <div class="feature" style="left:612px">
    <div class="icon"><svg width="64" height="60" viewBox="0 0 64 60"><rect x="2" y="24" width="14" height="34" fill="#9e0f12"/><path d="M20 26 34 4c4-2 8 1 7 6l-4 12h20c4 0 6 4 5 7l-6 24c-1 3-3 5-6 5H20z" fill="#9e0f12"/></svg></div>
    <h4>Trusted</h4><p>Duis autem vel eum iriure dolor in hendrerit in vulputate velit esse molestie conat .</p>
  </div>
  <div class="feature" style="left:886px">
    <div class="icon"><svg width="52" height="70" viewBox="0 0 52 70"><path d="M10 40 2 66l12-6 6 10 8-24zM42 40l8 26-12-6-6 10-8-24z" fill="#9e0f12"/><circle cx="26" cy="26" r="24" fill="#9e0f12"/><circle cx="26" cy="26" r="15" fill="#fff"/><path d="m26 15 3.3 7 7.4.8-5.6 5 1.6 7.3L26 31.3l-6.7 3.8 1.6-7.3-5.6-5 7.4-.8z" fill="#9e0f12"/></svg></div>
    <h4>Experience</h4><p>Duis autem vel eum iriure dolor in hendrerit in vulputate velit esse molestie conat .</p>
  </div>
</section>

<footer class="site-footer">
  <div class="col" style="left:80px;width:150px"><h5>Quick Links</h5>
    <ul class="links" style="margin-top:10px"><li>Home</li><li>About Us</li><li>Gallery</li><li>Testimonials</li><li>Contact Us</li></ul>
  </div>
  <div class="col contact" style="left:307px;width:240px"><h5>Contact Details</h5>
    <div class="row"><svg width="16" height="20" viewBox="0 0 16 20"><path d="M8 0a8 8 0 0 0-8 8c0 6 8 12 8 12s8-6 8-12a8 8 0 0 0-8-8z" fill="#b5161b"/><circle cx="8" cy="8" r="3" fill="#2a2a2a"/></svg><div><b>DOVIN PRATCHELL HOMES</b><br>12345 Lo 10th Iriure, Esse<br>Molestie, AB 01234</div></div>
    <div class="row"><svg width="16" height="16" viewBox="0 0 24 24"><path fill="#b5161b" d="M6.6 10.8a15 15 0 0 0 6.6 6.6l2.2-2.2c.3-.3.7-.4 1-.2 1.1.4 2.3.6 3.6.6.6 0 1 .4 1 1V20c0 .6-.4 1-1 1A17 17 0 0 1 3 4c0-.6.4-1 1-1h3.5c.6 0 1 .4 1 1 0 1.3.2 2.5.6 3.6.1.3 0 .7-.2 1z"/></svg>123 456 7890</div>
    <div class="row"><svg width="16" height="16" viewBox="0 0 24 24"><path fill="#b5161b" d="M6.6 10.8a15 15 0 0 0 6.6 6.6l2.2-2.2c.3-.3.7-.4 1-.2 1.1.4 2.3.6 3.6.6.6 0 1 .4 1 1V20c0 .6-.4 1-1 1A17 17 0 0 1 3 4c0-.6.4-1 1-1h3.5c.6 0 1 .4 1 1 0 1.3.2 2.5.6 3.6.1.3 0 .7-.2 1z"/></svg>123 456 7890</div>
    <div class="row"><svg width="16" height="12" viewBox="0 0 24 18"><path fill="#b5161b" d="M0 0h24v18H0z"/><path fill="none" stroke="#2a2a2a" stroke-width="2" d="M1 1l11 9 11-9"/></svg>info@dovinpratchellhomes.com</div>
  </div>
  <div class="col" style="left:625px;width:495px"><h5 style="border:none">Location Map</h5></div>
  <div class="map" role="img" aria-label="Street map showing the office location with a pin"></div>
</footer>

<div class="bottombar">
  <span>Copyright © 2017 Dovin Pratchell Homes. All Rights Reserved.</span>
  <div class="social"><span></span><span></span><span></span></div>
</div>

</body>
</html>
```